Webdesign for Brisvane for use on webpage

We aim to deliver insights for power consumers in the nordic market in the B2B market, without being a supplier.

Since we are helping customers in the green transition and reducing CO2 emissions, green colors would be preferred, but we are keeping an open mind. We would like to communicate transperancy, awareness and enabling economic potential for customers.

We deliver our product on a SaaS platform through visualization in dashboards

Target Market(s)

B2B

Industry/Entity Type

Power Consumption

Number of Pages Required

1 page

Colors
0054AA
0677BA
7BADD7
CADEEF
E8F1F8
0094D4
00A9DD
6FCCEA
C7EBF8
E9F6FB
00AB8E
00BBA5
67D7C9
C6EFE9
E9F9F6
59FF00
82FF00
B8FF75
E3FFCB
F4FFEA

Requirements
Must have
• The general looks and color schemes must be in line with logo called "brisvane.eps" - see attached

```html
<!DOCTYPE html>
<html lang="en">
<head>
<meta charset="utf-8">
<title>Brisvane — Energy Data Insights</title>
<link href="https://fonts.googleapis.com/css2?family=Montserrat:ital,wght@0,400;0,500;0,600;0,700;0,800;1,500&display=swap" rel="stylesheet">
<style>
:root{
  --navy:#0b3f9c;
  --blue:#0054aa;
  --sky:#c6d8ee;
  --lime:#59ff00;
  --lime-2:#4cf01f;
  --ink:#1a1a1a;
  --grey:#777;
  --white:#ffffff;
  --card-shadow:0 4px 14px rgba(0,0,0,.07);
}
*{box-sizing:border-box;margin:0;padding:0}
html,body{width:1200px;height:3496px;overflow:hidden;background:var(--white)}
body{position:relative;font-family:'Montserrat',sans-serif;color:var(--ink)}
.abs{position:absolute}

/* header */
.brand{left:143px;top:14px;width:180px;text-align:center}
.brand-mark{width:104px;height:104px;border:4px solid var(--blue);border-radius:50%;margin:0 auto 8px}
.brand-name{font-size:36px;font-weight:800;color:var(--blue);letter-spacing:1px;line-height:1}
.brand-tag{font-size:10px;font-weight:600;color:var(--lime-2);margin-top:4px}
.phone{left:601px;top:50px;display:flex;align-items:center;gap:8px;font-size:19px;font-weight:700;color:var(--blue)}
.btn{display:flex;align-items:center;justify-content:center;border-radius:30px;font-weight:700;color:var(--white);text-decoration:none}
.btn-login{left:820px;top:43px;width:114px;height:47px;background:var(--blue);font-size:16px}
.btn-signup{left:941px;top:43px;width:114px;height:47px;background:var(--lime);font-size:16px}
.nav{top:126px;font-size:16px;font-weight:700;color:#222}
.nav.active{color:var(--blue)}

/* hero */
.hero-title{left:143px;top:292px;font-size:72px;font-weight:800;line-height:77px;color:var(--ink)}
.hero-title .accent{color:var(--blue)}
.btn-start{left:144px;top:562px;width:195px;height:54px;background:var(--lime);font-size:19px;font-weight:600}
.hero-art{left:530px;top:217px;width:670px;height:435px;border-radius:50% 0 0 40%;background:radial-gradient(ellipse at 55% 50%,#dfe6fb 0%,#eef1fc 50%,#fff 80%)}
.scroll-cue{left:567px;top:652px}

/* section titles */
.section-title{left:0;width:1200px;text-align:center;font-size:42px;font-weight:800;color:var(--blue)}
.rule{width:55px;height:3px;background:var(--lime-2)}

/* offer cards */
.card{background:var(--white);box-shadow:var(--card-shadow);width:290px;height:292px;text-align:center;padding-top:20px}
.card-icon{width:80px;height:80px;margin:0 auto}
.card-title{margin-top:42px;font-size:16px;font-weight:700;color:var(--ink)}
.card-text{margin:16px auto 0;width:220px;font-size:12.5px;line-height:20px;color:var(--grey)}
.btn-view{left:504px;width:194px;height:52px;font-size:19px}

/* about */
.about-band{left:0;top:1724px;width:1200px;height:675px}
.about-art{left:129px;top:1914px;width:414px;height:502px;border-radius:30px;background:linear-gradient(160deg,#e9eef9 0%,#4a63e0 45%,#1f3cc6 70%,#f3f6fb 100%)}
.about-title{left:614px;top:1910px;font-size:42px;font-weight:800;color:var(--blue)}
.about-text{left:614px;top:2020px;width:440px;font-size:14.3px;line-height:21.7px;font-weight:500;color:var(--blue)}
.btn-read{left:612px;top:2245px;width:196px;height:52px;background:var(--blue);font-size:19px}

/* blog */
.post-photo{border-radius:0}
.post-card{left:166px;top:2828px;width:354px;height:198px;background:var(--white);box-shadow:var(--card-shadow);text-align:center;padding-top:24px}
.post-title{font-size:17px;font-weight:500;color:var(--ink)}
.post-meta{font-size:11px;color:var(--grey);display:flex;align-items:center;gap:6px}
.post-text{font-size:11px;line-height:22px;color:var(--grey)}
.post-link{font-size:14px;font-weight:700;color:var(--lime-2)}

/* footer */
.footer-name{left:143px;top:3400px;width:250px;text-align:center;font-size:50px;font-weight:800;color:var(--white);line-height:1}
.footer-tag{left:143px;top:3454px;width:250px;text-align:center;font-size:14px;font-weight:700;color:var(--white)}
.social{width:52px;height:52px;border:2px solid var(--white);border-radius:50%;top:3332px}
.copyright{left:513px;top:3422px;font-size:14px;color:var(--white)}
</style>
</head>
<body>

<!-- header -->
<div class="abs brand">
  <div class="brand-mark"></div>
  <div class="brand-name">BRISVANE</div>
  <div class="brand-tag">Energy data insights</div>
</div>

<div class="abs phone">
  <svg width="34" height="34" viewBox="0 0 34 34"><circle cx="17" cy="17" r="15.5" fill="none" stroke="#0054aa" stroke-width="2"/><path d="M12 10c1-1 2-1 2.5 0l1.5 3c.3.7 0 1.3-.6 1.7l-1 .7c.8 1.8 2.3 3.3 4.1 4.1l.7-1c.4-.6 1-.9 1.7-.6l3 1.5c1 .5 1 1.5 0 2.5-1.5 1.5-3.5 1.8-6 .3-2.8-1.7-4.8-3.7-6.3-6.3-1.4-2.5-1.1-4.4.4-5.9z" fill="#0054aa"/></svg>
  <span>1 555 010 2040</span>
</div>
<a class="abs btn btn-login">LOGIN</a>
<a class="abs btn btn-signup">SIGN UP</a>

<svg class="abs" style="left:450px;top:122px" width="22" height="24" viewBox="0 0 22 24"><path d="M11 3c4 0 7 3 7 7 0 3-2 4-3 6v3H7v-3c-1-2-3-3-3-6 0-4 3-7 7-7z" fill="none" stroke="#4cf01f" stroke-width="2"/><rect x="8" y="20" width="6" height="2" fill="#0054aa"/></svg>
<div class="abs nav active" style="left:481px">HOME</div>
<div class="abs nav" style="left:574px">ABOUT</div>
<div class="abs nav" style="left:675px">SERVICES</div>
<div class="abs nav" style="left:798px">NEWS</div>
<div class="abs nav" style="left:890px">CONTACT US</div>
<svg class="abs" style="left:1039px;top:127px" width="17" height="17" viewBox="0 0 17 17"><circle cx="7" cy="7" r="5" fill="none" stroke="#0054aa" stroke-width="2.5"/><path d="M11 11l4.5 4.5" stroke="#0054aa" stroke-width="2.5" stroke-linecap="round"/></svg>

<!-- hero -->
<div class="abs hero-art" role="img" aria-label="Isometric illustration of a SaaS platform: 3D letters, cloud, laptop dashboard, charts and magnifier"></div>
<h1 class="abs hero-title">ENERGY<br><span class="accent">DATA</span><br>INSIGHTS</h1>
<a class="abs btn btn-start">GET STARTED</a>
<svg class="abs scroll-cue" width="36" height="56" viewBox="0 0 36 56"><circle cx="18" cy="5" r="4" fill="none" stroke="#333" stroke-width="1.5"/><path d="M18 9v6" stroke="#333" stroke-width="1.5"/><circle cx="18" cy="35" r="16" fill="none" stroke="#333" stroke-width="1.5"/><path d="M18 24v20M12 38l6 6 6-6" fill="none" stroke="#333" stroke-width="1.5"/></svg>

<!-- what we offer -->
<h2 class="abs section-title" style="top:830px">WHAT WE OFFER</h2>
<div class="abs rule" style="left:573px;top:899px"></div>

<div class="abs card" style="left:143px;top:975px">
  <svg class="card-icon" viewBox="0 0 80 80"><rect x="6" y="8" width="66" height="64" rx="6" fill="none" stroke="#0054aa" stroke-width="3"/><path d="M6 22h66" stroke="#0054aa" stroke-width="3"/><circle cx="14" cy="15" r="2" fill="#4cf01f"/><circle cx="21" cy="15" r="2" fill="#4cf01f"/><circle cx="28" cy="15" r="2" fill="#4cf01f"/><path d="M28 38l-8 8 8 8M52 38l8 8-8 8M44 34l-8 24" fill="none" stroke="#0054aa" stroke-width="3"/></svg>
  <div class="card-title">LOREM IPSUM DOLOR</div>
  <p class="card-text">Sed ut perspiciatis unde omnis iste natus error sit volupt atem accusa ntium doloremque laudan tium totam rem apeed ut perspiciatis unde omnis iste natus error sit</p>
</div>
<div class="abs card" style="left:457px;top:975px">
  <svg class="card-icon" viewBox="0 0 80 80"><rect x="4" y="16" width="60" height="42" rx="3" fill="none" stroke="#0054aa" stroke-width="3"/><path d="M0 64h72" stroke="#0054aa" stroke-width="4"/><circle cx="62" cy="16" r="9" fill="none" stroke="#4cf01f" stroke-width="4"/><circle cx="62" cy="16" r="3" fill="#4cf01f"/></svg>
  <div class="card-title">SED UT PERSPICIA</div>
  <p class="card-text">Sed ut perspiciatis unde omnis iste natus error sit volupt atem accusa ntium doloremque laudan tium totam rem apeed ut perspiciatis unde omnis iste natus error sit</p>
</div>
<div class="abs card" style="left:770px;top:975px">
  <svg class="card-icon" viewBox="0 0 80 80"><rect x="30" y="4" width="16" height="70" transform="rotate(45 38 39)" fill="none" stroke="#0054aa" stroke-width="3"/><rect x="30" y="4" width="16" height="70" transform="rotate(-45 38 39)" fill="none" stroke="#4cf01f" stroke-width="3"/></svg>
  <div class="card-title">MAGNA ALIQUA</div>
  <p class="card-text">Sed ut perspiciatis unde omnis iste natus error sit volupt atem accusa ntium doloremque laudan tium totam rem apeed ut perspiciatis unde omnis iste natus error sit</p>
</div>

<div class="abs card" style="left:143px;top:1303px">
  <svg class="card-icon" viewBox="0 0 80 80"><path d="M18 52c-9 0-13-8-10-14 2-5 7-6 9-5 1-9 10-13 17-10 5-6 16-4 18 4 8-1 14 6 12 13-1 6-6 9-11 9" fill="none" stroke="#4cf01f" stroke-width="3.5"/><text x="21" y="44" font-family="Montserrat,sans-serif" font-weight="700" font-size="16" fill="#0054aa">CO</text><path d="M40 50c-4 6-6 9-6 13a6 6 0 0012 0c0-4-2-7-6-13z" fill="none" stroke="#0054aa" stroke-width="3"/></svg>
  <div class="card-title">ALIQUIP EX</div>
  <p class="card-text">Sed ut perspiciatis unde omnis iste natus error sit volupt atem accusa ntium doloremque laudan tium totam rem apeed ut perspiciatis unde omnis iste natus error sit</p>
</div>
<div class="abs card" style="left:457px;top:1303px">
  <svg class="card-icon" viewBox="0 0 80 80"><path d="M12 44c-6 0-8-10 0-12 0-10 10-14 16-9 4-10 22-10 26 0 10-2 16 6 14 14 4 4 2 7-2 7z" fill="#36b24a"/><text x="40" y="72" text-anchor="middle" font-family="Montserrat,sans-serif" font-weight="800" font-size="20" fill="#0054aa">SAAS</text></svg>
  <div class="card-title">DUIS AUTE IRURE</div>
  <p class="card-text">Sed ut perspiciatis unde omnis iste natus error sit volupt atem accusa ntium doloremque laudan tium totam rem apeed ut perspiciatis unde omnis iste natus error sit</p>
</div>
<div class="abs card" style="left:770px;top:1303px">
  <svg class="card-icon" viewBox="0 0 80 80"><rect x="10" y="30" width="60" height="42" fill="none" stroke="#0054aa" stroke-width="3"/><path d="M6 30l6-20h56l6 20z" fill="none" stroke="#4cf01f" stroke-width="3"/><path d="M22 10l-4 20M34 10l-2 20M46 10l2 20M58 10l4 20" stroke="#4cf01f" stroke-width="3"/><rect x="20" y="44" width="16" height="28" fill="none" stroke="#0054aa" stroke-width="3"/><rect x="44" y="44" width="18" height="14" fill="none" stroke="#0054aa" stroke-width="3"/></svg>
  <div class="card-title">REPREHENDERIT</div>
  <p class="card-text">Sed ut perspiciatis unde omnis iste natus error sit volupt atem accusa ntium doloremque laudan tium totam rem apeed ut perspiciatis unde omnis iste natus error sit</p>
</div>

<!-- about -->
<svg class="abs" style="left:0;top:1590px" width="1200" height="820" viewBox="0 0 1200 820"><circle cx="600" cy="378" r="358" fill="none" stroke="#c6d8ee" stroke-width="12"/></svg>
<svg class="abs about-band" viewBox="0 0 1200 675" preserveAspectRatio="none"><polygon points="0,149 1200,0 1200,675 0,675" fill="#59ff00"/></svg>
<a class="abs btn btn-view" style="top:1645px;background:var(--blue)">VIEW MORE</a>
<div class="abs about-art" role="img" aria-label="Desktop monitor showing an energy analytics dashboard, framed by a dark ring"></div>
<h2 class="abs about-title">ABOUT US</h2>
<div class="abs rule" style="left:614px;top:1981px;background:var(--white)"></div>
<p class="abs about-text">Lorem ipsum dolor sit amet, consectetur adipiscing elit, sed do eiusmod tempor incididunt ut labore et dolore magna aliqua. Quis ipsum suspendisse ultrices gravida. Risus commodo viverra maecenas accumsan lacus vel facilisis. Lorem ipsum dolor sit amet, consectetur adipiscing elit, sed do eiusmod tempor incididunt ut labore et dolore magna aliqua. Quis ipsum suspendisse ultrices gravida. Risus commodo viverra maecenas accumsan lacus vel facilisis. Lorem ipsum dolor sit amet, consectetur adipiscing elit, sed do eiusmod tempor</p>
<a class="abs btn btn-read">READ MORE</a>

<!-- blog -->
<h2 class="abs section-title" style="top:2491px;left:14px">BLOG POSTS</h2>
<div class="abs rule" style="left:587px;top:2562px"></div>

<div class="abs post-photo" style="left:141px;top:2625px;width:403px;height:261px;background:radial-gradient(circle at 55% 55%,#2f7a2a 0%,#1b2a22 35%,#111418 70%)" role="img" aria-label="Hand turning a glowing green CO2 emissions dial"></div>
<div class="abs post-card">
  <div class="post-title">Ut enim ad minima veniam,</div>
  <div class="post-meta" style="justify-content:center;margin-top:12px"><span style="color:#0054aa">●</span> Comments | <span style="color:#4cf01f">●</span> Admin</div>
  <p class="post-text" style="margin-top:12px">Sed ut perspiciatis unde omnis iste natus error sit<br>voluptatem accusantium doloremda</p>
  <div class="post-link" style="margin-top:14px">READ MORE</div>
</div>

<div class="abs post-photo" style="left:580px;top:2625px;width:195px;height:188px;background:linear-gradient(135deg,#9a7a5a,#c9ab86 50%,#6d5a46)" role="img" aria-label="Team working on laptops around a wooden table"></div>
<div class="abs post-title" style="left:797px;top:2643px">Ut enim ad minima veniam,</div>
<div class="abs post-meta" style="left:799px;top:2676px"><span style="color:#0054aa">●</span> Comments | <span style="color:#4cf01f">●</span> Admin</div>
<p class="abs post-text" style="left:799px;top:2709px">Sed ut perspiciatis unde omnis iste natus error sit<br>voluptatem accusantium doloremda</p>
<div class="abs post-link" style="left:797px;top:2776px">READ MORE</div>

<div class="abs post-photo" style="left:580px;top:2840px;width:195px;height:187px;background:linear-gradient(135deg,#d9d9d9,#8c8c8c 50%,#e8e8e8)" role="img" aria-label="Laptop showing charts on a desk with papers"></div>
<div class="abs post-title" style="left:797px;top:2857px">Ut enim ad minima veniam,</div>
<div class="abs post-meta" style="left:799px;top:2890px"><span style="color:#0054aa">●</span> Comments | <span style="color:#4cf01f">●</span> Admin</div>
<p class="abs post-text" style="left:799px;top:2918px">Sed ut perspiciatis unde omnis iste natus error sit<br>voluptatem accusantium doloremda</p>
<div class="abs post-link" style="left:797px;top:2990px">READ MORE</div>

<!-- footer -->
<svg class="abs" style="left:0;top:3030px" width="1200" height="466" viewBox="0 0 1200 466"><circle cx="903" cy="350" r="292" fill="none" stroke="#c6d8ee" stroke-width="12"/></svg>
<svg class="abs" style="left:0;top:3176px" width="1200" height="320" viewBox="0 0 1200 320" preserveAspectRatio="none"><polygon points="0,0 1200,150 1200,320 0,320" fill="#0b3f9c"/></svg>
<a class="abs btn btn-view" style="top:3103px;background:var(--lime)">VIEW MORE</a>

<div class="abs" style="left:196px;top:3242px;width:148px;height:148px;border:4px solid var(--white);border-radius:50%"></div>
<div class="abs footer-name">BRISVANE</div>
<div class="abs footer-tag">Energy data insights</div>

<div class="abs social" style="left:514px" aria-label="Social profile 1"></div>
<div class="abs social" style="left:581px" aria-label="Social profile 2"></div>
<div class="abs social" style="left:647px" aria-label="Social profile 3"></div>
<div class="abs social" style="left:714px" aria-label="Social profile 4"></div>

<div class="abs copyright">© Copyright 2021 Brisvane.All Rights Reserved &nbsp;| Privacy Policy &nbsp;| &nbsp;Terms and Use</div>

</body>
</html>
```